Brindle Structures Construction Company Seeking Modern Website

We are a small construction company wanting to create a web presence. We don't have much in the way of current content but will get photos as they come in. Attached is a picture of our business card.
The pages we would like on the menu are:
Home
Portfolio
Product Specs
Testimonials
Our Process
Contact
Some designs we like are:
http://www.tovenquarnsheds.example/
http://www.qzrsheds.example/
http://pannowsheds.example/
http://wistenhalls.example/
Not much requirements other than that so feel free to be creative!
Updates
Target Market(s)
Construction
Commercial and Residential Buildings
Industry/Entity Type
Construction Company
Number of Pages Required
5+ page
Look and feel

```html
<!DOCTYPE html>
<html lang="en">
<head>
<meta charset="utf-8">
<title>Brindle Structures</title>
<link rel="stylesheet" href="https://fonts.googleapis.com/css2?family=Roboto:ital,wght@0,300;0,400;0,500;0,700;0,900;1,400;1,900&display=swap">
<style>
:root{
  --blue:#1ba3de;
  --blue-dark:#0d7fb3;
  --ink:#0b0b0b;
  --text:#555;
  --muted:#777;
  --panel:#ececec;
  --footer:#242424;
  --footer-line:#3a3a3a;
  --white:#fff;
}
*{box-sizing:border-box;margin:0;padding:0}
html,body{width:1200px;height:2296px;overflow:hidden;background:var(--white)}
body{font-family:"Roboto",Arial,sans-serif;color:var(--text)}
.page{position:relative;width:1200px;height:2296px;overflow:hidden}
.abs{position:absolute}

/* header */
.topbar{left:0;top:0;width:1200px;height:93px;background:var(--white)}
.brand{left:73px;top:44px;display:flex;align-items:center;gap:14px}
.brand-dot{width:34px;height:34px;border-radius:50%;background:var(--blue)}
.brand-name{font-weight:900;font-size:44px;color:var(--blue);letter-spacing:-1px}
.callus{left:845px;top:22px;display:flex;gap:12px;align-items:center}
.callus-label{font-size:15px;font-weight:500;color:var(--ink);letter-spacing:.3px}
.callus-number{font-size:33px;color:var(--blue);line-height:1}
.navbar{left:0;top:93px;width:1200px;height:98px;background:var(--ink);border-bottom:5px solid var(--blue)}
.nav{left:73px;top:148px;display:flex;height:43px}
.nav a{display:block;color:var(--white);text-decoration:none;font-weight:500;font-size:17px;line-height:43px;padding:0 17px;margin-right:17px}
.nav a.is-active{background:var(--blue)}
.social-top{left:969px;top:146px;display:flex;gap:8px}
.social-top span{width:35px;height:35px;border:2px solid var(--white);border-radius:50%}

/* hero */
.hero{left:0;top:196px;width:1200px;height:707px;background:repeating-linear-gradient(45deg,#f1f1f1 0 2px,#e8e8e8 2px 5px)}
.slide{left:73px;top:220px;width:1053px;height:500px;background:linear-gradient(180deg,#4d80c8 0%,#8fb3de 32%,#c9b99b 55%,#7f8f55 80%,#4e6b2e 100%);border:1px solid #ccc}
.slide-arrow{top:413px;width:16px;height:115px;display:flex;align-items:center;justify-content:center}
.slide-arrow.prev{left:57px;background:#555}
.slide-arrow.next{left:1127px;background:var(--blue)}
.hero-copy{left:80px;top:768px;width:1040px;text-align:center;font-size:20.5px;line-height:28px;color:#555}

/* services */
.services{left:0;top:903px;width:1200px;height:620px;background:linear-gradient(180deg,#c9c9c9 0%,#eeeeee 35%,#fff 60%)}
.card{top:950px;width:514px}
.card-head{height:60px;background:var(--blue);display:flex;align-items:center;justify-content:center;gap:18px;color:var(--white);font-weight:900;font-style:italic;font-size:32px;letter-spacing:-.5px;position:relative}
.card-head::before,.card-head::after{content:"";position:absolute;bottom:-13px;border-top:13px solid var(--blue-dark)}
.card-head::before{left:0;border-left:11px solid transparent}
.card-head::after{right:0;border-right:11px solid transparent}
.card-body{margin:0 11px;height:455px;background:linear-gradient(180deg,#e6e6e6 0%,#f6f6f6 60%,#fff 100%);padding:18px 18px 0}
.card-photo{width:458px;height:262px}
.card-photo.residential{background:linear-gradient(180deg,#5e93d6 0%,#a9c8ec 40%,#c2a98a 60%,#8aa05d 80%,#8a8a8a 100%)}
.card-photo.commercial{background:linear-gradient(160deg,#3f7fd0 0%,#7fb7e8 40%,#d9dde2 70%,#b5b5b5 100%)}
.card-text{margin-top:18px;font-size:13.8px;line-height:21.5px;color:#555}
.btn{display:flex;align-items:center;height:46px;background:var(--blue-dark);color:var(--white);font-size:18px;text-decoration:none;clip-path:polygon(8px 0,100% 0,calc(100% - 8px) 100%,0 100%)}
.btn span{padding:0 22px 0 18px}
.btn i{height:100%;width:44px;background:#0b6d9c;display:flex;align-items:center;justify-content:center}
.btn-shadow{height:6px;background:radial-gradient(ellipse at center,rgba(0,0,0,.18),transparent 70%)}

/* testimonial + news */
.block-title{top:1605px;width:513px;height:52px;border-bottom:4px solid var(--blue-dark)}
.block-title h2{font-weight:900;font-style:italic;font-size:32px;color:var(--ink);letter-spacing:-1px}
.block-arrows{position:absolute;right:0;top:10px;display:flex;gap:10px}
.quote-mark{left:73px;top:1683px;width:48px;height:48px;background:#d9d9d9;display:flex;align-items:center;justify-content:center;font-size:48px;font-weight:900;color:#666;line-height:1;padding-top:16px}
.quote-text{left:137px;top:1693px;width:450px;font-style:italic;font-size:14px;line-height:21.5px;color:#555}
.author{left:133px;top:1807px;display:flex;gap:12px;align-items:center}
.author-avatar{width:54px;height:54px;border-radius:50%;border:3px solid var(--blue);background:linear-gradient(135deg,#c9d6e3,#8aa2ba)}
.author-name{font-size:15px;font-weight:500;color:var(--ink)}
.author-role{font-size:12.5px;color:var(--muted)}
.news-date{left:614px;top:1694px;font-size:12.5px;color:var(--muted)}
.news-title{left:614px;top:1713px;font-size:16.5px;font-weight:500;color:var(--blue-dark)}
.news-text{left:614px;top:1743px;width:512px;font-size:13.8px;line-height:21.5px;color:#555}

/* footer */
.footer-band{left:135px;top:1951px;width:930px;height:13px;background:var(--blue-dark);clip-path:polygon(8px 0,100% 0,calc(100% - 8px) 100%,0 100%)}
.footer{left:0;top:1964px;width:1200px;height:295px;background:var(--footer)}
.footer-col{top:2000px;width:243px;color:#ddd}
.footer-col+.footer-col{border-left:1px solid var(--footer-line)}
.footer-col h3{font-size:19px;font-weight:500;color:var(--white);padding-bottom:10px;border-bottom:1px solid var(--footer-line);margin-bottom:16px}
.links li{list-style:none;font-size:13.5px;line-height:26px;color:#ccc}
.contact-item{display:flex;gap:12px;font-size:13.5px;line-height:20px;color:#ccc;margin-bottom:17px}
.contact-item svg{flex:none;margin-top:3px}
.map{width:245px;height:153px;background:linear-gradient(135deg,#e9e4d6 0%,#d5dcc4 50%,#e7e2d4 100%);border:1px solid #555}
.keep li{list-style:none;display:flex;align-items:center;gap:12px;font-size:14.5px;color:#ddd;margin-bottom:11px}
.keep li span{width:35px;height:35px;border:2px solid #ddd;border-radius:50%}
.copyright{left:0;top:2259px;width:1200px;height:37px;background:#141414;font-size:12.5px;color:#aaa;padding:13px 0 0 76px}
</style>
</head>
<body>
<div class="page">

  <header>
    <div class="abs topbar"></div>
    <div class="abs brand"><span class="brand-dot"></span><span class="brand-name">Brindle Structures</span></div>
    <div class="abs callus">
      <svg width="38" height="40" viewBox="0 0 24 24" fill="none" stroke="#111" stroke-width="1.6"><path d="M5 3l4 1 1 4-2 2c1 3 3 5 6 6l2-2 4 1 1 4-2 2C10 21 3 14 3 5z"/></svg>
      <div><div class="callus-label">CALL US TODAY!</div><div class="callus-number">1.800.555.0142</div></div>
    </div>
    <div class="abs navbar"></div>
    <nav class="abs nav">
      <a class="is-active">HOME</a><a>PORTFOLIO</a><a>PRODUCT SPECS</a><a>TESTIMONIALS</a><a>OUR PROCESS</a><a>CONTACT</a>
    </nav>
    <div class="abs social-top"><span></span><span></span><span></span><span></span></div>
  </header>

  <section>
    <div class="abs hero"></div>
    <div class="abs slide" role="img" aria-label="Photo of a two-storey beige family home with porch, dormers and lawn"></div>
    <div class="abs slide-arrow prev"><svg width="7" height="10"><path d="M7 0L0 5l7 5z" fill="#fff"/></svg></div>
    <div class="abs slide-arrow next"><svg width="7" height="10"><path d="M0 0l7 5-7 5z" fill="#fff"/></svg></div>
    <p class="abs hero-copy">Lorem ipsum dolor sit amet, consectetur adipiscing elit, sed do eiusmod tempor incididunt ut labore et dolore magna aliqua. Ut enim ad minim veniam, quis nostrud exercitation ullamco laboris nisi ut aliquip ex ea commodo consequat. Duis aute irure dolor in reprehenderit in voluptate velit.</p>
  </section>

  <section>
    <div class="abs services"></div>

    <article class="abs card" style="left:73px">
      <div class="card-head">
        <svg width="38" height="34" viewBox="0 0 24 22" fill="#fff"><path d="M12 1L1 11h3v10h6v-6h4v6h6V11h3z"/></svg>Residental
      </div>
      <div class="card-body">
        <div class="card-photo residential" role="img" aria-label="Photo of a street of new suburban houses"></div>
        <p class="card-text">Sed ut perspiciatis unde omnis iste natus error sit voluptatem accusantium doloremque laudantium, totam rem aperiam, eaque ipsa quae ab illo inventore veritatis et quasi architecto beatae vitae dicta sunt explicabo. Nemo enim ipsam voluptatem quia voluptas sit aspernatur aut odit aut fugit, sed quia consequuntur magni dolores eos qui ratione voluptatem sequi nesciunt.</p>
      </div>
    </article>
    <a class="abs btn" style="left:245px;top:1482px"><span>Learn more</span><i><svg width="10" height="16"><path d="M1 1l7 7-7 7" stroke="#fff" stroke-width="2.5" fill="none"/></svg></i></a>
    <div class="abs btn-shadow" style="left:160px;top:1526px;width:340px"></div>

    <article class="abs card" style="left:614px">
      <div class="card-head">
        <svg width="36" height="46" viewBox="0 0 18 24" fill="#fff"><path d="M2 2h14v22h-5v-4H7v4H2z"/><g fill="#1ba3de"><rect x="4" y="5" width="3" height="3"/><rect x="11" y="5" width="3" height="3"/><rect x="4" y="10" width="3" height="3"/><rect x="11" y="10" width="3" height="3"/><rect x="4" y="15" width="3" height="3"/><rect x="11" y="15" width="3" height="3"/></g></svg>Commercial
      </div>
      <div class="card-body">
        <div class="card-photo commercial" role="img" aria-label="Photo of a curved glass office building"></div>
        <p class="card-text">Sed ut perspiciatis unde omnis iste natus error sit voluptatem accusantium doloremque laudantium, totam rem aperiam, eaque ipsa quae ab illo inventore veritatis et quasi architecto beatae vitae dicta sunt explicabo. Nemo enim ipsam voluptatem quia voluptas sit aspernatur aut odit aut fugit, sed quia consequuntur magni dolores eos qui ratione voluptatem sequi nesciunt.</p>
      </div>
    </article>
    <a class="abs btn" style="left:785px;top:1482px"><span>Learn more</span><i><svg width="10" height="16"><path d="M1 1l7 7-7 7" stroke="#fff" stroke-width="2.5" fill="none"/></svg></i></a>
    <div class="abs btn-shadow" style="left:700px;top:1526px;width:340px"></div>
  </section>

  <section>
    <div class="abs block-title" style="left:73px">
      <h2>Testimonial</h2>
      <div class="block-arrows"><svg width="10" height="18"><path d="M9 1L2 9l7 8" stroke="#666" stroke-width="3" fill="none"/></svg><svg width="10" height="18"><path d="M1 1l7 8-7 8" stroke="#1ba3de" stroke-width="3" fill="none"/></svg></div>
    </div>
    <div class="abs quote-mark">&ldquo;</div>
    <p class="abs quote-text">Sed ut perspiciatis unde omnis iste natus error sit voluptatem accusantium doloremque laudantium, totam rem aperiam, eaque ipsa quae ab illo inventore veritatis et quasi architecto beatae vitae dicta sunt explicabo. Nemo enim ipsam voluptatem quia voluptas sit aspernatur aut odit aut fugit.</p>
    <div class="abs author">
      <div class="author-avatar" role="img" aria-label="Customer portrait"></div>
      <div><div class="author-name">Dana Whitlow</div><div class="author-role">Happy Customer</div></div>
    </div>

    <div class="abs block-title" style="left:614px">
      <h2>Latest News</h2>
      <div class="block-arrows"><svg width="10" height="18"><path d="M9 1L2 9l7 8" stroke="#666" stroke-width="3" fill="none"/></svg><svg width="10" height="18"><path d="M1 1l7 8-7 8" stroke="#1ba3de" stroke-width="3" fill="none"/></svg></div>
    </div>
    <div class="abs news-date">10 Nov 2015</div>
    <div class="abs news-title">Sed ut perspiciatis unde omnis iste natus error sit.</div>
    <p class="abs news-text">Voluptatem accusantium doloremque laudantium, totam rem aperiam, eaque ipsa quae ab illo inventore veritatis et quasi architecto beatae vitae dicta sunt explicabo. totam rem aperiam, eaque ipsa quae ab illo inventore veritatis et quasi architecto beatae vitae dicta sunt explicabo. totam rem aperiam, eaque ipsa quae.</p>
    <a class="abs btn" style="left:614px;top:1864px;height:38px;font-size:14px"><span>Learn more</span><i style="width:36px"><svg width="9" height="14"><path d="M1 1l6 6-6 6" stroke="#fff" stroke-width="2.5" fill="none"/></svg></i></a>
  </section>

  <footer>
    <div class="abs footer-band"></div>
    <div class="abs footer"></div>

    <div class="abs footer-col" style="left:73px;border:0;padding-right:16px">
      <h3>Quick Links</h3>
      <ul class="links"><li>Home</li><li>Portfolio</li><li>Product Specs</li><li>Testimonials</li><li>Our Process</li><li>Contact</li></ul>
    </div>
    <div class="abs footer-col" style="left:331px;padding:0 16px 30px 12px">
      <h3>Contact Address</h3>
      <div class="contact-item"><svg width="11" height="15" viewBox="0 0 12 16"><path d="M6 0a6 6 0 0 1 6 6c0 4-6 10-6 10S0 10 0 6a6 6 0 0 1 6-6z" fill="#ddd"/><circle cx="6" cy="6" r="2" fill="#242424"/></svg><span>228, Lorem Ipsum dolor sit,<br>Dosis amet sit - 85485</span></div>
      <div class="contact-item"><svg width="13" height="13" viewBox="0 0 24 24" fill="#ddd"><path d="M5 2l4 1 1 5-2 2c1 3 3 5 6 6l2-2 5 1 1 4-3 3C10 22 2 14 2 5z"/></svg><span>Call Us<br>1.800.555.0142</span></div>
      <div class="contact-item"><svg width="13" height="10" viewBox="0 0 14 10"><rect width="14" height="10" fill="#ddd"/><path d="M0 0l7 6 7-6" stroke="#242424" fill="none"/></svg><span>Email Us<br>info@brindlestructures.example</span></div>
    </div>
    <div class="abs footer-col" style="left:600px;padding:0 12px 60px 13px">
      <h3>Location Map</h3>
      <div class="map" role="img" aria-label="Street map showing the office location"></div>
    </div>
    <div class="abs footer-col" style="left:871px;padding:0 0 60px 12px;width:256px">
      <h3>Keep In Touch</h3>
      <ul class="keep"><li><span></span>Fanpage</li><li><span></span>Chirper</li><li><span></span>Circles +</li><li><span></span>Linkwork</li></ul>
    </div>

    <div class="abs copyright">Copyright © 2015 Brindle Structures. | Terms of Use &nbsp;| &nbsp;Privacy Policy &nbsp;| &nbsp;Sitemap</div>
  </footer>

</div>
</body>
</html>
```